Web page design for podiatry office*

Need a web page for our podiatry office. It should feature most of our services, hours, directions and location. Should include a short bio of the doctor and a contact page.

Coding

Coded - Design and coding required

Number of Pages Required

1 page

Colors

Designer to choose colors to be used in the design.

```html
<!DOCTYPE html>
<html lang="en">
<head>
<meta charset="utf-8">
<title>Stridewell – Foot &amp; Ankle Care</title>
<link href="https://fonts.googleapis.com/css2?family=Mulish:ital,wght@0,400;0,600;0,700;0,800;1,400&display=swap" rel="stylesheet">
<style>
:root{
  --blue:#2f8fd8;
  --blue-dark:#1f6fb8;
  --ink:#1d2430;
  --text:#555c66;
  --muted:#8a919b;
  --line:#e6e8eb;
  --soft:#f7f7f8;
  --navy:#34465d;
  --footer:#2b3b52;
  --footer-box:#243246;
  --star:#f7c325;
}
*{box-sizing:border-box;margin:0;padding:0}
html,body{width:1200px;height:2875px;overflow:hidden}
body{font-family:"Mulish",sans-serif;color:var(--text);background:#fff;font-size:10px;position:relative}
.wrap{position:absolute;left:235px;width:731px}
section,header,footer,nav{position:absolute;left:0;width:1200px}
a{color:inherit;text-decoration:none}

/* top bar */
.topbar{top:0;height:59px;border-bottom:1px solid var(--line)}
.brand{position:absolute;left:235px;top:14px;display:flex;align-items:center;gap:10px;font-weight:800;font-size:16px;color:var(--blue);letter-spacing:.3px}
.brand .mark{width:30px;height:30px;background:var(--blue)}
.info{position:absolute;top:18px;display:flex;gap:9px;align-items:flex-start;white-space:nowrap}
.info svg{flex:none}
.info b{display:block;font-weight:600;color:var(--ink);font-size:10px}
.info span{display:block;color:var(--muted);font-size:9px;margin-top:1px}
.socials{display:flex;gap:3px;margin-top:3px}
.socials i{width:10px;height:10px;border-radius:50%;background:#b8bec6;display:block}

.nav{top:59px;height:40px;border-bottom:1px solid var(--line)}
.nav ul{position:absolute;left:235px;top:0;display:flex;gap:24px;list-style:none;height:40px;align-items:center;font-size:9px;font-weight:700;color:var(--ink)}
.nav li.active{color:var(--blue)}
.nav .search{position:absolute;left:749px;top:0;width:42px;height:40px;border-left:1px solid var(--line);display:flex;align-items:center;justify-content:center}
.nav .book{position:absolute;left:791px;top:0;width:134px;height:40px;background:var(--blue);color:#fff;font-size:9px;font-weight:700;display:flex;align-items:center;justify-content:center}
.nav .menu{position:absolute;left:925px;top:0;width:41px;height:40px;border-right:1px solid var(--line);display:flex;align-items:center;justify-content:center}

/* hero */
.hero{top:99px;height:432px;background:linear-gradient(90deg,#e9eaec 0%,#e4e6e9 45%,#d8d4d0 70%,#c9a58c 100%)}
.hero-photo{position:absolute;left:540px;top:0;width:660px;height:432px;background:linear-gradient(110deg,rgba(230,232,235,0) 0%,rgba(214,200,190,.6) 55%,rgba(200,150,120,.75) 100%)}
.hero .eyebrow{position:absolute;left:235px;top:150px;color:var(--blue);font-weight:600;font-size:11px}
.hero h1{position:absolute;left:235px;top:174px;font-weight:600;font-size:19px;line-height:25px;color:var(--ink)}
.btn{display:inline-flex;align-items:center;justify-content:center;background:var(--blue);color:#fff;font-weight:700;font-size:9px;border-radius:2px}
.hero .btn{position:absolute;left:235px;top:242px;width:219px;height:32px}
.arrow{position:absolute;top:194px;width:44px;height:44px;border-radius:50%;background:rgba(180,186,194,.5);display:flex;align-items:center;justify-content:center}

/* headings */
.sec-title{position:absolute;left:0;width:1200px;text-align:center;font-weight:800;font-size:19px;color:var(--ink);letter-spacing:.3px}
.sec-lead{position:absolute;left:360px;width:480px;text-align:center;font-size:9px;line-height:15px;color:var(--text)}

/* about */
.about{top:531px;height:509px}
.about .copy{top:160px;width:360px;font-size:10px;line-height:15px}
.about .copy h3{font-size:10px;font-weight:700;color:var(--ink);line-height:15px;margin-bottom:14px}
.about .copy em{display:block;margin-bottom:14px}
.about .copy p{margin-bottom:15px}
.about .copy .btn{width:89px;height:31px;margin-top:4px}
.ph{position:absolute}
.ph1{left:631px;top:170px;width:188px;height:187px;background:linear-gradient(135deg,#6d4a3f,#cfc6c0)}
.ph2{left:822px;top:285px;width:144px;height:144px;background:linear-gradient(135deg,#d9b8a5,#f1e4dc)}
.ph3{left:723px;top:360px;width:96px;height:96px;background:linear-gradient(135deg,#3b3e44,#c2573a)}

/* services */
.services{top:1040px;height:430px;background:var(--soft)}
.cards{top:146px;display:flex;gap:19px}
.card{width:169px;height:221px;background:#fff;box-shadow:0 1px 3px rgba(0,0,0,.06)}
.card .img{height:106px}
.card h4{margin:16px 8px 6px 15px;font-size:9.5px;font-weight:700;color:var(--ink);white-space:nowrap;letter-spacing:-.1px}
.card p{margin:0 15px;font-size:8.5px;line-height:15px}
.card a{display:block;margin:9px 15px 0;font-size:8.5px;font-weight:700;color:var(--blue)}

/* cta */
.cta{top:1470px;height:271px;background:linear-gradient(90deg,#3a4d66,#2f435c 60%,#34475f);color:#fff;text-align:center}
.cta .q{position:absolute;top:58px;width:1200px;font-size:15px;font-weight:600}
.cta h2{position:absolute;top:84px;width:1200px;font-size:28px;font-weight:600}
.cta .call{position:absolute;top:124px;width:1200px;font-size:19px;font-weight:600}
.cta .btn{position:absolute;left:529px;top:178px;width:142px;height:31px;font-size:10px}

/* clients */
.clients{top:1741px;height:441px}
.quotes{top:167px;display:flex;gap:19px}
.quote{width:231px}
.quote .bubble{height:147px;background:var(--blue);border-radius:3px;color:#fff;padding:24px 15px 0;font-size:10px;line-height:15px}
.stars{display:flex;gap:3px;margin-top:11px}
.person{display:flex;justify-content:flex-end;align-items:center;gap:11px;margin-top:16px}
.person b{display:block;font-weight:600;color:var(--ink);font-size:11px;text-align:right}
.person span{display:block;font-size:9px;color:var(--muted);text-align:right}
.avatar{width:44px;height:44px;border-radius:50%;background:linear-gradient(135deg,#b8a090,#6c5a50)}

/* map */
.map{top:2182px;height:320px;background:linear-gradient(135deg,#eef0e6,#f3f1e8 50%,#ebede3)}
.contact-box{position:absolute;left:235px;top:60px;width:188px;height:199px;background:var(--blue);color:#fff;padding:38px 30px 0}
.contact-box h3{font-size:13px;font-weight:600;margin-bottom:20px}
.crow{display:flex;gap:12px;align-items:flex-start;font-size:9px;line-height:13px;margin-bottom:20px;white-space:nowrap}
.crow svg{flex:none}

/* footer */
.footer{top:2502px;height:373px;background:var(--footer);color:#c5ccd6}
.footer .brand{top:56px;color:var(--blue)}
.f-about{position:absolute;left:235px;top:105px;width:190px;font-size:9px;line-height:15px}
.f-social{position:absolute;left:235px;top:208px;display:flex;gap:7px}
.f-social i{width:25px;height:25px;border:1px solid var(--blue);border-radius:50%;display:block}
.fcol h5{font-size:11px;font-weight:600;color:#fff;margin-bottom:30px}
.fcol{position:absolute;top:55px}
.links{list-style:none;font-size:9px}
.links li{margin-bottom:11px;display:flex;gap:10px;align-items:center}
.links li:before{content:"";width:8px;height:1px;background:var(--blue)}
.hours{position:absolute;left:779px;top:46px;width:187px;height:233px;background:var(--footer-box);padding:26px 17px 0}
.hours .ring{position:absolute;left:72px;top:-18px;width:40px;height:40px;border-radius:50%;background:var(--footer);display:flex;align-items:center;justify-content:center}
.hrow{display:flex;justify-content:space-between;font-size:9px;color:#fff;margin-bottom:14.5px}
.hrow b{font-weight:700}
.hours .btn{width:156px;height:28px;margin-top:11px;font-size:9px}
.f-bottom{position:absolute;left:235px;top:321px;width:731px;display:flex;justify-content:space-between;font-size:8.5px;border-top:1px solid #3a4a62;padding-top:17px}
.f-bottom span+span{margin-left:22px}
</style>
</head>
<body>

<header class="topbar">
  <div class="brand"><span class="mark"></span>STRIDEWELL</div>
  <div class="info" style="left:428px">
    <svg width="20" height="20" viewBox="0 0 20 20" fill="none" stroke="#2f8fd8" stroke-width="1.3"><circle cx="10" cy="11" r="7"/><path d="M10 7v4l3 2M4 4l2-2M16 4l-2-2"/></svg>
    <div><b>Monday - Friday 8:00 - 20:00</b><span>Saturday and Sunday - CLOSED</span></div>
  </div>
  <div class="info" style="left:610px">
    <svg width="14" height="20" viewBox="0 0 14 20" fill="none" stroke="#2f8fd8" stroke-width="1.3"><rect x="1" y="1" width="12" height="18" rx="2"/><path d="M5 16h4"/></svg>
    <div><b>+ 8000 555 0142</b><span>office@stridewell.example</span></div>
  </div>
  <div class="info" style="left:742px">
    <svg width="14" height="20" viewBox="0 0 14 20" fill="none" stroke="#2f8fd8" stroke-width="1.3"><path d="M7 19s6-7 6-11A6 6 0 0 0 1 8c0 4 6 11 6 11z"/><circle cx="7" cy="8" r="2.2"/></svg>
    <div><b>Harbor Lane 12</b><span>Springfield, US</span></div>
  </div>
  <div class="info" style="left:873px">
    <svg width="22" height="18" viewBox="0 0 22 18" fill="none" stroke="#2f8fd8" stroke-width="1.3"><path d="M1 8h5l8-6 1 2-4 3h9v3h-3v2h-2v2h-2v2H7L1 14z"/></svg>
    <div><b>Follow Us</b><div class="socials"><i></i><i></i><i></i><i></i></div></div>
  </div>
</header>

<nav class="nav">
  <ul>
    <li class="active">HOME</li><li>ABOUT US</li><li>SERVICES</li><li>NEW VISITORS</li><li>CONTACT US</li>
  </ul>
  <div class="search"><svg width="12" height="12" viewBox="0 0 12 12" fill="none" stroke="#555c66" stroke-width="1.3"><circle cx="7" cy="5" r="4"/><path d="M4 8L1 11"/></svg></div>
  <a class="book">BOOK APPOINTMENT</a>
  <div class="menu"><svg width="13" height="9" viewBox="0 0 13 9" stroke="#555c66" stroke-width="1.2"><path d="M0 1h13M0 4.5h13M0 8h13"/></svg></div>
</nav>

<section class="hero">
  <div class="hero-photo" role="img" aria-label="Podiatrist in gloves examining a patient's foot with a magnifying glass"></div>
  <div class="arrow" style="left:93px"><svg width="8" height="10" viewBox="0 0 8 10" fill="none" stroke="#fff" stroke-width="1.5"><path d="M6 1L2 5l4 4"/></svg></div>
  <div class="arrow" style="left:1047px"><svg width="8" height="10" viewBox="0 0 8 10" fill="none" stroke="#fff" stroke-width="1.5"><path d="M2 1l4 4-4 4"/></svg></div>
  <div class="eyebrow">WELCOME TO STRIDEWELL</div>
  <h1>High-Quality Foot &amp; Ankle Care and<br>In-Office Surgical Treatments</h1>
  <a class="btn">RESERVE YOUR CONSULTATION TODAY!</a>
</section>

<section class="about">
  <h2 class="sec-title" style="top:56px">ABOUT US</h2>
  <p class="sec-lead" style="top:90px">Lorem ipsum dolor sit amet, consectetuer. Proin gravida nibh vel velit auctor aliquetenean. Cum sociis Theme natoque penatibus et magnis dis parturient nascetur ridiculus mus</p>
  <div class="wrap copy">
    <h3>LOREM IPSUM DOLOR SIT AMET, CONSECTETUR ADIPISCING ELIT.<br>ETIAM ULTRICES LEO VITAE ANTE PHARETRA</h3>
    <em>Donec at erat porttitor, venenatis erat eu, malesuada eros. Curabitur nec metus enim. Vestibulum lacinia sollicitudin justo.</em>
    <p>Nunc ultricies vel elit ut sagittis. Nulla in massa et mi auctor viverra. Sed interdum sed dolor non aliquet. Morbi rhoncus risus vel est molestie, quis commodo ipsum suscipit. Duis molestie massa vel blandit pharetra. Integer finibus est et lorem maximus interdum. Ut vel neque est.</p>
    <p>Aenean non mattis eros. Aliquam accumsan nunc quis scelerisque aliquet. Etiam nulla tortor, faucibus a scelerisque ac, porta ac libero. Proin posuere ex lacus, a interdum turpis hendrerit et. Curabitur pharetra, sapien nec ornare pretium, purus ex luctus erat, quis sodales neque sem ut nulla.</p>
    <a class="btn">LEARN MORE</a>
  </div>
  <div class="ph ph1" role="img" aria-label="Doctor with stethoscope consulting a patient"></div>
  <div class="ph ph2" role="img" aria-label="Hands examining a bare foot"></div>
  <div class="ph ph3" role="img" aria-label="Runner's ankle with highlighted pain area"></div>
</section>

<section class="services">
  <h2 class="sec-title" style="top:52px">OUR SERVICES</h2>
  <p class="sec-lead" style="top:86px">Lorem ipsum dolor sit amet, consectetuer. Proin gravida nibh vel velit auctor aliquetenean. Cum sociis Theme natoque penatibus et magnis dis parturient nascetur ridiculus mus</p>
  <div class="wrap cards">
    <div class="card"><div class="img" role="img" aria-label="Podiatrist treating a toenail" style="background:linear-gradient(135deg,#cfd6dc,#e8d7cb)"></div><h4>ADVANCED PODIATRY</h4><p>Lorem ipsum dolor sit amet, consectetur adipiscing elit. Etiam ultrices leo vitae ante pharetra.</p><a>READ MORE</a></div>
    <div class="card"><div class="img" role="img" aria-label="Doctor holding a patient's foot" style="background:linear-gradient(135deg,#e9e6e3,#d7c2b3)"></div><h4>AT RISK FOOT CARE</h4><p>Lorem ipsum dolor sit amet, consectetur adipiscing elit. Etiam ultrices leo vitae ante pharetra.</p><a>READ MORE</a></div>
    <div class="card"><div class="img" role="img" aria-label="Athlete's ankle with highlighted injury" style="background:linear-gradient(135deg,#3a3d42,#b4533b 60%,#4a4c50)"></div><h4>SPORTS MEDICINE</h4><p>Lorem ipsum dolor sit amet, consectetur adipiscing elit. Etiam ultrices leo vitae ante pharetra.</p><a>READ MORE</a></div>
    <div class="card"><div class="img" role="img" aria-label="Sole of a foot with highlighted pain area" style="background:linear-gradient(135deg,#c89a84,#e06a60 55%,#7d6a60)"></div><h4>FOOT AND ANKLE SURGERY</h4><p>Lorem ipsum dolor sit amet, consectetur adipiscing elit. Etiam ultrices leo vitae ante pharetra.</p><a>READ MORE</a></div>
  </div>
</section>

<section class="cta" role="img" aria-label="Dark blue band with a faint photo of a foot examination">
  <div class="q">Need a Doctor for Check-up?</div>
  <h2>Just make an Appointment &amp; You’re Done!</h2>
  <div class="call">Get Your Quote or Call: 8000 555 014</div>
  <a class="btn">GET AN APPOINTMENT</a>
</section>

<section class="clients">
  <h2 class="sec-title" style="top:64px">OUR CLIENTS SAY</h2>
  <p class="sec-lead" style="top:98px">Lorem ipsum dolor sit amet, consectetuer. Proin gravida nibh vel velit auctor aliquetenean. Cum sociis Theme natoque penatibus et magnis dis parturient nascetur ridiculus mus</p>
  <div class="wrap quotes">
    <div class="quote"><div class="bubble">“Lorem ipsum dolor sit amet, consectetur adipiscing elit. Etiam ultrices leo vitae ante pharetra, at convallis massa placerat. Curabitur vel neque et nisi mollis malesuada id sit amet lacus”
      <div class="stars"><svg width="60" height="9" viewBox="0 0 60 9" fill="#f7c325"><g id="st"><path d="M4.5 0l1.4 2.9 3.1.4-2.3 2.2.6 3.1-2.8-1.5-2.8 1.5.6-3.1L0 3.3l3.1-.4z"/></g><use href="#st" x="12"/><use href="#st" x="24"/><use href="#st" x="36"/><use href="#st" x="48"/></svg></div></div>
      <div class="person"><div><b>Dana Reyes</b><span>Client</span></div><div class="avatar" role="img" aria-label="Client portrait"></div></div></div>
    <div class="quote"><div class="bubble">“Lorem ipsum dolor sit amet, consectetur adipiscing elit. Etiam ultrices leo vitae ante pharetra, at convallis massa placerat. Curabitur vel neque et nisi mollis malesuada id sit amet lacus”
      <div class="stars"><svg width="60" height="9" viewBox="0 0 60 9" fill="#f7c325"><use href="#st"/><use href="#st" x="12"/><use href="#st" x="24"/><use href="#st" x="36"/><use href="#st" x="48"/></svg></div></div>
      <div class="person"><div><b>Dana Reyes</b><span>Client</span></div><div class="avatar" role="img" aria-label="Client portrait" style="background:linear-gradient(135deg,#4a3a36,#b08a7a)"></div></div></div>
    <div class="quote"><div class="bubble">“Lorem ipsum dolor sit amet, consectetur adipiscing elit. Etiam ultrices leo vitae ante pharetra, at convallis massa placerat. Curabitur vel neque et nisi mollis malesuada id sit amet lacus”
      <div class="stars"><svg width="60" height="9" viewBox="0 0 60 9" fill="#f7c325"><use href="#st"/><use href="#st" x="12"/><use href="#st" x="24"/><use href="#st" x="36"/><use href="#st" x="48"/></svg></div></div>
      <div class="person"><div><b>Dana Reyes</b><span>Client</span></div><div class="avatar" role="img" aria-label="Client portrait" style="background:linear-gradient(135deg,#e0cdb8,#9aa8b4)"></div></div></div>
  </div>
</section>

<section class="map" role="img" aria-label="Road map showing the office location">
  <svg style="position:absolute;left:583px;top:124px" width="26" height="36" viewBox="0 0 26 36"><path d="M13 35S25 20 25 12A12 12 0 0 0 1 12c0 8 12 23 12 23z" fill="#1fb3b0"/><circle cx="13" cy="12" r="5" fill="none" stroke="#fff" stroke-width="2.5"/></svg>
  <div class="contact-box">
    <h3>CONTACT INFO</h3>
    <div class="crow"><svg width="13" height="19" viewBox="0 0 14 20" fill="none" stroke="#fff" stroke-width="1.3"><path d="M7 19s6-7 6-11A6 6 0 0 0 1 8c0 4 6 11 6 11z"/><circle cx="7" cy="8" r="2.2"/></svg><div>Harbor Lane 12<br>Springfield, US</div></div>
    <div class="crow"><svg width="13" height="19" viewBox="0 0 14 20" fill="none" stroke="#fff" stroke-width="1.3"><rect x="1" y="1" width="12" height="18" rx="2"/><path d="M5 16h4"/></svg><div style="padding-top:3px">+ 8000 555 0142</div></div>
    <div class="crow"><svg width="20" height="17" viewBox="0 0 20 17" fill="none" stroke="#fff" stroke-width="1.3"><path d="M1 7l9-6 9 6v9H1z"/><path d="M1 7l9 6 9-6"/></svg><div style="padding-top:3px">office@stridewell.example</div></div>
  </div>
</section>

<footer class="footer">
  <div class="brand"><span class="mark"></span>STRIDEWELL</div>
  <p class="f-about">Lorem ipsum dolor sit amet, consectetur adipiscing elit. Etiam ultrices leo vitae ante pharetra, at convallis massa placerat. Curabitur vel neque et nisi mollis malesuada id sit amet lacus</p>
  <div class="f-social"><i></i><i></i><i></i><i></i></div>
  <div class="fcol" style="left:473px">
    <h5>QUICK LINKS</h5>
    <ul class="links"><li>Home</li><li>About us</li><li>Services</li><li>Careers</li><li>Medical Legal</li><li>Contact us</li></ul>
  </div>
  <div class="fcol" style="left:610px;width:160px">
    <h5>CONTACT INFO</h5>
    <div class="crow"><svg width="13" height="19" viewBox="0 0 14 20" fill="none" stroke="#2f8fd8" stroke-width="1.3"><path d="M7 19s6-7 6-11A6 6 0 0 0 1 8c0 4 6 11 6 11z"/><circle cx="7" cy="8" r="2.2"/></svg><div>Harbor Lane 12<br>Springfield, US</div></div>
    <div class="crow"><svg width="13" height="19" viewBox="0 0 14 20" fill="none" stroke="#2f8fd8" stroke-width="1.3"><rect x="1" y="1" width="12" height="18" rx="2"/><path d="M5 16h4"/></svg><div style="padding-top:3px">+ 8000 555 0142</div></div>
    <div class="crow"><svg width="20" height="17" viewBox="0 0 20 17" fill="none" stroke="#2f8fd8" stroke-width="1.3"><path d="M1 7l9-6 9 6v9H1z"/><path d="M1 7l9 6 9-6"/></svg><div style="padding-top:3px">office@stridewell.example</div></div>
  </div>
  <div class="hours">
    <div class="ring"><svg width="20" height="20" viewBox="0 0 20 20" fill="none" stroke="#2f8fd8" stroke-width="1.4"><circle cx="10" cy="11" r="7"/><path d="M10 7v4l3 2M4 4l2-2M16 4l-2-2"/></svg></div>
    <div class="hrow"><b>Monday</b><span>8:00 - 20:00</span></div>
    <div class="hrow"><b>Tuesday</b><span>8:00 - 20:00</span></div>
    <div class="hrow"><b>Wednesday</b><span>8:00 - 20:00</span></div>
    <div class="hrow"><b>Thursday</b><span>8:00 - 20:00</span></div>
    <div class="hrow"><b>Friday</b><span>8:00 - 20:00</span></div>
    <div class="hrow"><b>Saturday - Sunday</b><span>Closed</span></div>
    <a class="btn">MAKE AN APPOINTMENT</a>
  </div>
  <div class="f-bottom"><span>Copyright © 2019 Stridewell. All Right Reserved.</span><div><span>Terms &amp; Condition</span><span>Privacy Policy</span></div></div>
</footer>

</body>
</html>
```